Talcott Land Surveyors Business Card

We are a land surveying company looking for a business card with a clean, sharp design. We would like for our design to portray our logo on one side, and contact information on the other w/ or w/o logo. Our colors preferred are navy blue, grey/silver, white and black. thank you!

Industry/Entity Type

Surveyor

Contact Information for Business Card

Talcott Land Surveyors
Gordon Pavlikova, P.L.S.
(781) 555-0193
Talcottlandsurveyors@mailbox.example
Talcottlandsurveyors.example
287 Willowmere Lane, Reading MA 01999

Requirements
Must have
• 1. Company Name
2. Personal name and title
3. phone number
4. email.
5. website
6. address

```html
<!DOCTYPE html>
<html lang="en">
<head>
<meta charset="utf-8">
<title>Talcott Land Surveyors Business Card</title>
<link rel="stylesheet" href="https://fonts.googleapis.com/css2?family=Michroma&family=Roboto:ital,wght@0,400;1,700&display=swap">
<style>
  :root {
    --page: #2a2a2c;
    --card: #1b1b1c;
    --navy: #3a3fb0;
    --silver: #b9bcc2;
    --white: #f2f2f2;
  }
  * { margin: 0; padding: 0; box-sizing: border-box; }
  html, body { width: 1200px; height: 900px; overflow: hidden; background: var(--page); }
  .canvas {
    width: 1200px; height: 900px;
    display: flex; flex-direction: column; align-items: center; justify-content: center; gap: 40px;
  }
  .card {
    width: 700px; height: 400px; background: var(--card);
    position: relative; box-shadow: 0 10px 30px rgba(0,0,0,.45);
  }
  .brand {
    display: flex; align-items: center; gap: 18px;
    font-family: "Michroma", sans-serif; color: var(--navy);
    text-transform: uppercase; letter-spacing: 0.12em; line-height: 1.25;
  }
  .brand-mark {
    border: 3px solid var(--silver); border-radius: 50%; flex: none;
  }
  .card--logo { display: flex; align-items: center; justify-content: center; }
  .card--logo .brand { font-size: 34px; }
  .card--logo .brand-mark { width: 90px; height: 90px; }
  .card--contact .brand {
    position: absolute; left: 50px; top: 40px; font-size: 22px;
  }
  .card--contact .brand-mark { width: 48px; height: 48px; border-width: 2px; }
  .contact {
    position: absolute; left: 50px; top: 150px;
    font-family: "Roboto", sans-serif; color: var(--white); font-size: 16px; line-height: 1.55;
  }
  .contact-name { color: var(--navy); font-style: italic; font-weight: 700; font-size: 22px; }
  .contact-company { margin-bottom: 14px; }
  .contact-address { margin-bottom: 14px; }
  .contact-line { display: flex; align-items: center; gap: 10px; }
  .contact-line svg { width: 14px; height: 14px; fill: var(--navy); flex: none; }
</style>
</head>
<body>
<main class="canvas">
  <section class="card card--logo">
    <div class="brand">
      <span class="brand-mark"></span>
      <span class="brand-name">Talcott<br>Land Surveyors</span>
    </div>
  </section>

  <section class="card card--contact">
    <div class="brand">
      <span class="brand-mark"></span>
      <span class="brand-name">Talcott<br>Land Surveyors</span>
    </div>
    <div class="contact">
      <p class="contact-name">Gordon Pavlikova, P.L.S.</p>
      <p class="contact-company">Talcott Land Surveyors</p>
      <p class="contact-address">287 Willowmere Lane<br>Reading MA 01999</p>
      <p class="contact-line">
        <svg viewBox="0 0 24 24" aria-hidden="true"><path d="M6.6 10.8a15 15 0 0 0 6.6 6.6l2.2-2.2a1 1 0 0 1 1-.25 11.4 11.4 0 0 0 3.6.57 1 1 0 0 1 1 1V20a1 1 0 0 1-1 1A17 17 0 0 1 3 4a1 1 0 0 1 1-1h3.5a1 1 0 0 1 1 1c0 1.25.2 2.45.57 3.57a1 1 0 0 1-.25 1z"/></svg>
        (781) 555-0193
      </p>
      <p class="contact-line">
        <svg viewBox="0 0 24 24" aria-hidden="true"><path d="M2 5h20v14H2z M2 5l10 8 10-8" /></svg>
        Talcottlandsurveyors@mailbox.example
      </p>
      <p class="contact-line">
        <svg viewBox="0 0 24 24" aria-hidden="true"><circle cx="12" cy="12" r="10"/></svg>
        Talcottlandsurveyors.example
      </p>
    </div>
  </section>
</main>
</body>
</html>
```